Wordpress Design Project - MarbleQuay

I would like our existing old website at www.marblequay.example to be redesigned to a more modern attractive site using Wordpress, a total of 5 web pages. And also installed onto our new web hosting site. Please visit the existing website using Microsoft Internet explorer to see the content.
The new site must be compatible with all popular web browsers and mobile devices (if possible).
There should be a contact button available on each page with an associated form in case an interested person wants to contact us. This form must be spam proof not allowing automated crawlers from activating it.

There are only 5 pages web pages to this MarbleQuay project.

```html
<!DOCTYPE html>
<html lang="en">
<head>
<meta charset="utf-8">
<title>MarbleQuay</title>
<link rel="stylesheet" href="https://fonts.googleapis.com/css2?family=Noto+Serif:ital,wght@0,400;1,400&family=Open+Sans:wght@300;400;600&family=Roboto:wght@400&display=swap">
<style>
:root{
  --page:#f4f4f5;
  --white:#ffffff;
  --ink:#1e1e1e;
  --body:#4a4a4a;
  --muted:#9a9a9a;
  --faint:#d2d2d2;
  --line:#dedede;
  --brand:#1553a3;
  --leaf-dark:#5f9a0e;
  --leaf-light:#b9e03a;
}
*{margin:0;padding:0;box-sizing:border-box}
html,body{width:841px;height:1200px;overflow:hidden}
body{background:var(--page);font-family:"Noto Serif",serif;color:var(--body);position:relative}
.abs{position:absolute}

.masthead{left:0;top:0;width:841px;height:160px;background:linear-gradient(#fff,#f7f7f8)}
.brand{left:320px;top:62px;display:flex;align-items:center;gap:12px}
.brand-mark{width:38px;height:38px;border-radius:50%;background:var(--brand)}
.brand-name{font-family:"Open Sans",sans-serif;font-weight:600;font-size:26px;color:var(--brand)}

.main-nav{left:18px;top:157px;width:805px;height:33px;background:var(--white);border-top:1px solid var(--line);border-bottom:1px solid var(--line);display:flex;justify-content:center;align-items:center;gap:17px;font-size:11px;letter-spacing:.1px;color:var(--ink)}
.main-nav .current{font-style:italic;color:var(--muted)}

.slider{left:18px;top:210px;width:805px;height:317px;border:3px solid #e6e6e6;background:#fff;box-shadow:0 2px 4px rgba(0,0,0,.12)}
.slider-photo{width:100%;height:100%;background:radial-gradient(ellipse at 70% 35%,var(--leaf-light),#8fc322 45%,var(--leaf-dark) 100%)}
.caption{left:75px;top:287px;width:296px;height:287px;background:linear-gradient(#f2f2f2,#dcdcdc);border:1px solid #cfcfcf;box-shadow:-6px 8px 14px rgba(0,0,0,.18)}
.caption-inner{left:7px;top:12px;width:281px;height:258px;border:1px solid #fff}
.caption-title{left:27px;top:24px;font-family:"Open Sans",sans-serif;font-weight:300;font-size:27px;line-height:34px;color:#a3a3a3}
.caption-rule{left:7px;top:108px;width:281px;border-top:1px solid #c9c9c9;border-bottom:1px solid #fff}
.caption-text{left:26px;top:124px;width:258px;font-style:italic;font-size:10.4px;line-height:16px;color:#555}
.caption-btn{left:115px;top:266px;width:84px;height:30px;border-radius:15px;background:linear-gradient(#b5b5b5,#8e8e8e);color:#fff;font-style:italic;font-size:10.5px;text-align:center;line-height:30px;border:1px solid #fff}

.thumb{top:486px;width:77px;height:77px;border:4px solid #fff;box-shadow:0 6px 8px -4px rgba(0,0,0,.35)}
.thumb-a{left:451px;background:linear-gradient(135deg,#f3b845,#8c5a16)}
.thumb-b{left:543px;top:474px;background:linear-gradient(#d2ee5e,#6fa81a)}
.thumb-c{left:636px;background:linear-gradient(120deg,#e7e2d6,#4d4535)}
.thumb-d{left:728px;background:radial-gradient(circle at 40% 40%,#2a68d6,#08257c)}

.quote-mark{font-family:"Noto Serif",serif;font-size:54px;line-height:1;color:#222;font-weight:700}
.quote-open{left:17px;top:608px}
.quote-close{left:794px;top:664px}
.quote-text{left:48px;top:632px;font-size:18.5px;color:var(--ink)}
.quote-sub{left:48px;top:657px;font-family:"Open Sans",sans-serif;font-weight:300;font-size:20px;color:var(--faint)}

.tagline{left:0;top:727px;width:841px;height:49px;background:linear-gradient(#f7f7f7,#e8e8e8);border-top:1px solid var(--line);text-align:center;font-style:italic;font-size:14px;line-height:49px;color:#8a8a8a}

.content{left:18px;top:776px;width:805px;height:343px;background:var(--white);border:1px solid var(--line)}
.notch{left:665px;top:-1px}

.col-icon{width:30px;height:34px}
.col-title{font-family:"Open Sans",sans-serif;font-weight:300;font-size:17px;line-height:18px;color:var(--ink)}
.col-text{font-size:10.4px;line-height:16px;color:#555}
.more{height:17px;padding:0 8px;border-radius:9px;background:linear-gradient(#fff,#ececec);border:1px solid #ddd;font-family:"Roboto",sans-serif;font-size:8.5px;line-height:15px;color:#555}

.field{left:582px;width:176px;height:26px;border:1px solid #cfcfcf;border-radius:4px;background:#fff;font-family:"Roboto",sans-serif;font-size:11px;color:#333;padding:6px 8px}
.btn{top:275px;height:29px;border:1px solid #aaa;border-radius:4px;font-family:"Roboto",sans-serif;font-size:10.5px;color:#333;text-align:center;line-height:27px}
.btn-submit{left:641px;width:60px;background:linear-gradient(#e8e8e8,#c2c2c2)}
.btn-reset{left:707px;width:51px;background:linear-gradient(#fff,#e6e6e6)}

.credits{right:18px;top:1152px;font-style:italic;font-size:9.5px;color:var(--muted)}
.credits b{font-weight:400;color:#666}
</style>
</head>
<body>

<header class="abs masthead">
  <div class="abs brand"><span class="brand-mark"></span><span class="brand-name">MarbleQuay</span></div>
</header>

<nav class="abs main-nav">
  <span class="current">HOME</span>
  <span>TELEPHONE VOIP SOLUTION</span>
  <span>IP, LAN AND INTERNET</span>
  <span>SUPPORT SERVICES</span>
  <span>CONTACT US</span>
</nav>

<section class="abs slider">
  <div class="slider-photo" role="img" aria-label="Close-up of a ladybird climbing a bright green leaf"></div>
</section>

<div class="abs thumb thumb-a" role="img" aria-label="Thumbnail: golden wheat ear"></div>
<div class="abs thumb thumb-b" role="img" aria-label="Thumbnail: ladybird on green leaf"></div>
<div class="abs thumb thumb-c" role="img" aria-label="Thumbnail: bamboo stems"></div>
<div class="abs thumb thumb-d" role="img" aria-label="Thumbnail: dandelion seeds on blue"></div>

<article class="abs caption">
  <div class="abs caption-inner"></div>
  <h2 class="abs caption-title" style="font-weight:300">Advanced Features<br>Give You Control</h2>
  <div class="abs caption-rule"></div>
  <p class="abs caption-text">Sed nec eros orci, in facilisis mi. Cras lorem massa, viverra at dapibus id, posuere euismod elit. Mauris libero nisl, iaculis et tincidunt non, dapibus vitae ligula. In pharetra faucibus eros, at rhoncus leo sollicitudin quis. Vestibulum quis arcu non urna ultrices vestibulum. Fusce facilisis quam ut ipsum imperdiet eu ullamcorper orci volutpat. Vivamus vitae neque odio. Aenean convallis, augue...</p>
  <div class="abs caption-btn">READ MORE</div>
</article>

<div class="abs quote-mark quote-open">&ldquo;</div>
<p class="abs quote-text">Let our telecom engineers craft a solution that is custom designed to your specific needs.</p>
<p class="abs quote-sub">We're here to guide you</p>
<div class="abs quote-mark quote-close">&rdquo;</div>

<div class="abs tagline">Your Network Expert! What are you waiting for? Let us help you succeed.</div>

<main class="abs content">
  <svg class="abs notch" width="36" height="18" viewBox="0 0 36 18"><polygon points="0,0 36,0 18,18" fill="#ececec"/></svg>

  <svg class="abs col-icon" style="left:26px;top:31px" viewBox="0 0 30 34">
    <rect x="2" y="4" width="26" height="29" rx="2" fill="#8a6a44"/>
    <rect x="5" y="7" width="20" height="23" fill="#fff"/>
    <rect x="10" y="1" width="10" height="6" rx="1" fill="#bbb"/>
    <path d="M7 13l2 2 3-4M7 19l2 2 3-4M7 25l2 2 3-4" stroke="#3a9a2a" stroke-width="1.3" fill="none"/>
    <path d="M14 13h8M14 19h8M14 25h8" stroke="#999" stroke-width="1"/>
  </svg>
  <h3 class="abs col-title" style="left:73px;top:41px">Why MarbleQuay?</h3>
  <p class="abs col-text" style="left:73px;top:67px;width:188px">MarbleQuay provides state of the art VoIP PBX phone solutions with products tailored to small, medium, and large businesses. Our engineering team will asses your communication requirements and provide you with the best designed solution for your business needs.<br>MarbleQuay will be there for you during the whole process. From the initial quote all the way through installation and support. MarbleQuay is committed to you!</p>
  <div class="abs more" style="left:213px;top:291px">read more</div>

  <svg class="abs col-icon" style="left:282px;top:31px" viewBox="0 0 30 34">
    <rect x="2" y="4" width="22" height="27" fill="#fff" stroke="#aaa"/>
    <path d="M6 11h14M6 16h14M6 21h10" stroke="#aaa" stroke-width="1"/>
    <path d="M12 26L27 8l3 3-15 18-4 1z" fill="#f0b323" stroke="#7a5a10" stroke-width=".8"/>
  </svg>
  <h3 class="abs col-title" style="left:329px;top:41px">Kestrel's Voxline<br>SMB IP PBX</h3>
  <p class="abs col-text" style="left:329px;top:85px;width:185px">The Kestrel Voxline SMB powered by the Harborline IP Telephony engine is an award winning PBX switch line that gives you a rich host of features from interactive voice mail and video calling to linking up your ClearPhone and DarkPlum.</p>
  <div class="abs more" style="left:468px;top:212px">read more</div>

  <h3 class="abs col-title" style="left:582px;top:40px">Contact us</h3>
  <div class="abs field" style="top:56px">Name</div>
  <div class="abs field" style="top:83px">Email Address</div>
  <div class="abs field" style="top:110px">Subject</div>
  <div class="abs field" style="top:140px;height:122px"></div>
  <div class="abs btn btn-submit">SUBMIT</div>
  <div class="abs btn btn-reset">RESET</div>
</main>

<footer class="abs credits">Designed by <b>Orchardworks</b> | Powered by <b>Orchardworks</b></footer>

</body>
</html>
```